Taking a Paper and turning into a wonderful White Paper for Prospects and Clients

This is a white paper I need designed. I am including my company brochure so you can see the design/fonts being used and I'm including a white paper created - one that I like very much.

I am "NOT" looking for a cookie cutter white paper. I'm looking for a nice, clean design but with some creativity. Check out the white paper I included and you will get the idea.

Also included:
- the paper to be designed
- the paper to be designed "WITH" suggested design features such as carve outs, call outs and such

A few things I "DO NOT" like:
- images that are cheesy or corny
* people sitting at a table in a meeting
* Buildings

The white paper I included did not use pictures but had more design created by the firm. I like this approach and will probably give something like this more weight but is not required.

Reason: Realized time frame was too tight

Target Market(s)

Higher-End, wealthier clients

Industry/Entity Type

It Company

Requirements
Must have
• I DO NOT want the copy to be bunched together. The layout should flow where the copy is broken in the right spots to make reading easier. If you read a paper and it is just copy, interest is lost by everyone.
• COLORS: you can see from what I have included the colors I use
• My preference are very balanced colors using "clean spacing"

```html
<!DOCTYPE html>
<html lang="en">
<head>
<meta charset="utf-8">
<title>Is Your Financial Advisor a Fiduciary? – Tessaro</title>
<link href="https://fonts.googleapis.com/css2?family=Montserrat:wght@300;400;600;700&family=Libre+Baskerville:ital,wght@0,700;1,400&display=swap" rel="stylesheet">
<style>
:root{
  --page:#e9e9ec;
  --paper:#ffffff;
  --ink:#3b3b44;
  --navy:#15254d;
  --accent:#f08a24;
  --quote-bg:#e6ecf5;
  --rule:#c9c9d2;
  --link:#1b2f66;
}
*{box-sizing:border-box;margin:0;padding:0}
html,body{width:1200px;height:5294px;overflow:hidden}
body{background:var(--page);font-family:'Montserrat',sans-serif;font-weight:300;color:var(--ink);font-size:15.5px;line-height:1.62}
.topnote{height:46px;text-align:center;font-size:12px;padding-top:14px;color:var(--ink)}
.topnote a{color:var(--accent);text-decoration:none}
.paper{position:absolute;left:72px;top:46px;width:1056px;height:5210px;background:var(--paper);padding:40px 56px}
.rule-double{border-top:2px solid var(--navy);border-bottom:1px solid var(--navy);height:5px;margin-bottom:26px}
h1{font-weight:700;font-size:24px;line-height:1.3;color:var(--navy);text-transform:uppercase;margin-bottom:18px}
p{margin-bottom:20px}
.dots{list-style:none;margin:0 0 20px}
.dots li{position:relative;padding-left:22px;margin-bottom:4px}
.dots li::before{content:"";position:absolute;left:0;top:6px;width:11px;height:11px;border-radius:50%;background:var(--navy)}
.dots.small li::before{width:9px;height:9px;top:7px}
.quote{display:flex;gap:28px;background:var(--quote-bg);padding:20px 30px;margin-bottom:24px}
.quote svg{flex:none;margin-top:4px}
.quote h3{font-family:'Libre Baskerville',serif;font-size:17px;color:var(--navy);margin-bottom:4px}
.quote em{font-family:'Libre Baskerville',serif;font-size:15px}
.source{font-weight:700;font-style:italic;font-size:14px;color:var(--navy);text-decoration:underline;margin-bottom:26px;display:block}
.lead{font-weight:700;color:var(--navy);margin-bottom:4px}
.dashed{border-top:2px dashed var(--rule);margin:30px 0}
.table{width:100%;border-collapse:collapse;margin:30px 0 36px}
.table th{background:var(--navy);color:#fff;text-align:left;font-size:15px;font-weight:700;text-transform:uppercase;padding:16px 26px}
.table td{vertical-align:top;padding:26px 26px;border-bottom:1px solid var(--rule);width:50%}
.table td:first-child{border-right:1px solid var(--rule)}
.table td p{margin-bottom:18px}
h2{font-weight:700;font-size:19px;color:var(--navy);margin-bottom:12px}
.brand{font-weight:700;color:var(--navy)}
.services{list-style:none;margin-top:24px;border-left:2px solid var(--navy);margin-left:8px}
.services li{position:relative;padding:0 0 22px 34px}
.services li::before{content:"";position:absolute;left:-7px;top:5px;width:12px;height:12px;border-radius:50%;background:var(--navy)}
.services strong{font-weight:700;color:var(--navy)}
</style>
</head>
<body>
<div class="topnote">For anything about this mail you can contact us by <a href="#">visit this link</a>.</div>
<main class="paper">
  <div class="rule-double"></div>
  <h1>Is your financial advisor a fiduciary? It's not that simple…</h1>
  <ul class="dots">
    <li>Well, we say, the question is not whether your financial advisor is a fiduciary.</li>
    <li>The question is whether your financial advisor is consistently acting in your best interest.</li>
  </ul>
  <p>As an investor, you've almost certainly heard talk about the differences between "the fiduciary standard" and "the suitability standard," applied – largely – to advisors, brokers and other financial professionals.</p>
  <p>In fact, most likely you've heard (read) — umpteen times — that unless your financial advisors are fiduciaries, required by law to adhere to the fiduciary standard, they won't consistently act with your best interests in mind.</p>

  <div class="quote">
    <svg width="36" height="30" viewBox="0 0 36 30" aria-hidden="true"><path d="M0 30V16C0 7 5 1 14 0v6C9 7 7 11 7 15h7v15zM21 30V16c0-9 5-15 14-16v6c-5 1-7 5-7 9h7v15z" fill="#15254d"/></svg>
    <div><h3>From MARKET LEDGER, by Lionel Sterne:</h3><em>"Why Your Financial Advisor Should Be a Fiduciary"</em></div>
  </div>
  <div class="quote">
    <svg width="36" height="30" viewBox="0 0 36 30" aria-hidden="true"><path d="M0 30V16C0 7 5 1 14 0v6C9 7 7 11 7 15h7v15zM21 30V16c0-9 5-15 14-16v6c-5 1-7 5-7 9h7v15z" fill="#15254d"/></svg>
    <div><h3>From Civic News Hour, by Howard Pellman:</h3><em>"Why you should make sure your financial advisor abides by the fiduciary standard"</em></div>
  </div>
  <span class="source">https://www.civicnewshour.org/economy/column-make-sure-financial-advisor-abides-by-fiduciary-standard</span>

  <p>Nonetheless, some investors may, for any number of reasons, still choose to hire professionals who work under the suitability standard.</p>
  <p>But, the question remains: should you only hire an advisor acting as a fiduciary and avoid those who are not?</p>
  <p>Here at Tessaro – where we audit advisors for our clients covering areas such as fees charged, performance delivered, and investments used – we make certain our clients have great advisors.</p>
  <p>But, our paramount demand, made of all the advisors we audit is – the Financial Advisor "Acts in our client's best interest".</p>
  <p>When – working on your behalf – we audit the Registered Investment Advisors, Wealth Managers, Private Bankers, Trust Officers, Brokers or whatever other titles the financial professional may have, what concerns us is that they:</p>
  <ul class="dots small">
    <li>be honest with you</li>
    <li>provide you with sound advice</li>
    <li>look out for your best interest</li>
    <li>offer advice for a fair fee, "or" fair compensation;</li>
  </ul>
  <p class="lead">and then, above all:</p>
  <ul class="dots small"><li>we must be able to verify that your advisors are consistently doing the right things for you.</li></ul>

  <div class="dashed"></div>

  <p>Let us now tell you a cautionary tale. This story illustrates some eventual pitfalls of choosing financial advisors based solely on whether they work under the fiduciary standard.</p>
  <p>Three sports stars – Premier Baseball League pitchers Ray Oskins and Jack Peale, and NGL quarterback Mark Santos – believed they were bringing their "A-game" to the search for a great, trustworthy financial advisor.</p>
  <p>Arun Navarro, the financial advisor they chose, seemed to be made of all the right stuff. He worked for the Fort Ridge-based Ridgeline Capital Wealth Advisors. According to his business bio and cards, he was a Certified Public Account. The NGL Players Association had endorsed him. Furthermore, he regularly attended the same church as Santos and had an interest in charity work.</p>
  <p>Arun Navarro, nonetheless, turned out to be ruinously unscrupulous. He was not, in fact, a CPA. By fraudulent means, he transferred money out of his clients' accounts, often without their consent, into The Seat Exchange, a financially distressed company. And as a Seat Exchange board member, Navarro had multiple, egregious conflicts of interest that he never disclosed to his clients. By the time the deceitful scheme was uncovered and stopped, Navarro had misdirected $33 million of the three athletes' money and nearly all of it was lost.</p>
  <p>One crucial fact got left out of most of the reporting on that story, namely, that Arun Navarro was a fiduciary.</p>
  <p>As a Registered Investment Advisor working through Ridgeline Capital Management, Navarro was legally required to put his clients' interests before his own and to act in their best interests. He failed to do that. Subsequently, the Federal Securities Board filed a lawsuit against him and he settled without his clients being fully reimbursed.</p>
  <p>Was this avoidable? Tessaro tells you "Yes, this was avoidable." What happened to Mark Santos does not have to happen to you. Tessaro pro-actively verifies that your financial advisors are consistently acting in your best interest.</p>
  <p>The fine points in the differences between "the fiduciary standard" and "the suitability standard" are important for all of us to know, to be sure, but what's most important for now is to understand that the mere fact of an advisor being a fiduciary <strong style="font-weight:700;text-decoration:underline;color:var(--navy)">does not guarantee</strong> that the adviser will do the right things for you.</p>
  <p>After all, on the surface, Arun Navarro seemed like a trustworthy professional. He said he was a Certified Public Accountant. He worked through Ridgeline Capital Wealth Advisors. He was endorsed by the NGL Players Association. And he regularly attended the same church as Mark Santos. Had you asked him "Are you a fiduciary?" he would have said "Yes."</p>
  <p>Tessaro understands the daunting challenges investors face in trying to verify that their current or potential future financial advisors are trustworthy. Our deep, broad knowledge of the field allows us to develop our world-class system for auditing your financial advisors. Here is a sampling of the steps we would have taken had Mark Santos been our client.</p>

  <table class="table">
    <tr><th>Problem with Navarro</th><th>Tessaro's steps to protect you</th></tr>
    <tr>
      <td>Navarro misrepresented himself as a CPA, but was not one.</td>
      <td><p>We perform thoroughgoing background checks for every single credential an advisor claims.</p><p style="margin:0">We thoroughly verify claims about both educational background and professional certifications.</p></td>
    </tr>
    <tr>
      <td>Navarro improperly diverted Santos's funds.</td>
      <td><p>We obtain your account statements showing assets held, and any transfers.</p><p>In Santos's case, we would have seen the transfers to The Seat Exchange, and then verified with Santos that he had authorized those transfers for the reported amounts.</p><p>Additionally, when an advisor makes outside investments for our clients, we dig deeper else.</p><p>Why was the investment bought? Who has control of the investment? How are the assets valued and audited?</p><p style="margin:0">We answer those kinds of questions. We can clearly explain to you why we posed each question and what we think of the answer.</p></td>
    </tr>
    <tr>
      <td>Navarro's superiors at Ridgeline Capital failed to provide adequate ethical oversight of his work.</td>
      <td>We would have been evaluating how Ridgeline Capital's management structure provides oversight and auditing of what its advisors are doing for their clients.</td>
    </tr>
    <tr>
      <td>Navarro was endorsed by the NGL Players Association.</td>
      <td><p>Whatever the source of such an endorsement be it a players association, a listing in the Financial Ledger Top 400 list, or Bramwell's Top 100 Advisors, etc. — we view it with thewaryinvestor.com</p><p>Why?</p><p>These organizations base their advisor rankings on limited metrics such as the number of years an advisor has been in the industry and the types of clients the advisor has.</p><p style="margin:0">Those metrics are of small import for an individual investor. Such limited metrics comprise less than 10% of what Tessaro looks at when evaluating financial advisors.</p></td>
    </tr>
  </table>

  <p>Remember, the right question is not whether your financial advisor is a fiduciary. The right question is whether your advisor is consistently acting in your best interest.</p>

  <div class="dashed"></div>

  <h2>Who are we?</h2>
  <p style="margin-bottom:4px">We are <span class="brand">TESSARO</span> – a client advocacy firm working on behalf of our clients to make certain they have hired, or will hire, a great financial advisor.</p>
  <p style="margin-bottom:4px">With over 600,000 registered advisors in the United States, how do you know the advisor you might choose is one of the best?</p>
  <p>We have four core areas clients entrust us to help:</p>
  <ul class="services">
    <li><strong>EVALUATE</strong> your current financial advisor in 16+ areas; fee's being charged, investment returns, investment products being used, background check on the advisor and firm, to name a few.</li>
    <li><strong>FIND</strong> a great financial advisor with a customized search based on your needs and goals but making certain the advisor delivers good, risk-based returns for a fair fee.</li>
    <li><strong>PERFORMANCE GUARD</strong> focused on periodic check-ups on your investments and returns. We provide you comfort in knowing your advisor is investing correctly, with the right products and the right fees.</li>
    <li style="padding-bottom:0"><strong>ADVISOR BACKGROUND CHECK</strong> helps you understand who you are working with currently or who you might hire; do they have the right experience, client complaints or fines, are they truthful in what they said about education, credentials, and background? We verify this information on behalf of our clients.</li>
  </ul>
</main>
</body>
</html>
```